12 Page Catalog Design.. Only Front Cover and Two Pages needed for contest

We are looking to have a catalog designed for approximately 50 of our products that are in 5 different categories...

The product photos will be added to pages that have lifestyle shots and other graphics that you as the designer incorporate.

The catalog will be 12 pages long including a cover, history of our company, several lifestyle shots and placeholders for our product images.

As for a deliverable we would expect something in either InDesign or Adobe Illustrator.

Thanks..

Target Market(s)

Our market is mostly preppy and yachtie.. We also have a large buying group in the area of tennis.. Think resorts, country clubs, higher income..

Industry/Entity Type

It Company

Font styles to use
Serif
Sans Serif

Requirements
Must have
• Must incorporate our design logo into the design which would include the actual logo (below as both .PDF and .AI) as well as the key colors (orange and blue) which are part of the logo.

We will have the following components:
1. Front Cover
2. Back Cover
3. Several Lifestyle Shots integrated into catalog
4. Five Categories (Totes, Handbags, Travel, Sports, Tech Accessories)
5. Page telling about the company history.

As mentioned above, the contest is for the front cover, company story page and two pages for templates. Once we pick the winner we would ask that the winner complete the templates for the other pages and do the back cover.

The catalog will be 12 pages (8.5" x 11").

The files should be completed in either Illustrator or InDesign.

I'll add in photos of our last catalog for reference... It was only 4 pages.

We would like the photos to be at least twice the size as before. Our product images are all Hi_Res on our website at www.morlandquist.com.

This is our first time using something like this so any questions please ask..

Should not have
• Should not be too busy. Must be clean, simple and elegant.

```html
<!DOCTYPE html>
<html lang="en">
<head>
<meta charset="utf-8">
<title>Morland Quist Catalog – Cover and Story Spread</title>
<link rel="stylesheet" href="https://fonts.googleapis.com/css2?family=Roboto+Condensed:ital,wght@0,300;0,400;0,700;1,300&family=Cormorant+Garamond:wght@600&display=swap">
<style>
  :root {
    --orange: #cf5a2a;
    --blue: #2a5194;
    --navy: #1f3f7a;
    --ink: #2b2b2b;
    --white: #ffffff;
    --paper: #ffffff;
    --sans: "Roboto Condensed", "Arial Narrow", sans-serif;
    --serif: "Cormorant Garamond", Georgia, serif;
  }
  * { box-sizing: border-box; margin: 0; padding: 0; }
  html, body { width: 1000px; height: 1200px; overflow: hidden; background: var(--paper); }
  body { position: relative; font-family: var(--sans); color: var(--ink); }
  .abs { position: absolute; }
  .page { position: absolute; background: var(--white); box-shadow: 2px 3px 6px rgba(0,0,0,.35); overflow: hidden; }

  /* ---------- Front cover ---------- */
  .cover { left: 342px; top: 41px; width: 384px; height: 543px; }
  .photo-beach { left: 0; top: 0; width: 124px; height: 149px; background: linear-gradient(160deg, #6f9fd0 0%, #c9b39a 55%, #e7d2c0 100%); }
  .photo-sail { left: 0; top: 151px; width: 124px; height: 228px; background: linear-gradient(180deg, #4f86c8 0%, #dfe8f0 45%, #2b6aa6 75%, #1c4f86 100%); }
  .photo-tote { left: 134px; top: 0; width: 250px; height: 379px; background: linear-gradient(160deg, #c8d8e6 0%, #f2f2f0 40%, #3a5fae 70%, #8aa7c5 100%); }
  .cover-rule { left: 125px; top: 0; width: 6px; height: 379px; background: var(--orange); }
  .photo-flag { left: 0; top: 381px; width: 384px; height: 30px; background: linear-gradient(90deg, #2c4f8f 0%, #3d5e9b 45%, #e9e5e3 60%, #c2333a 75%, #f0e9e6 88%, #b8333a 100%); }
  .photo-family { left: 0; top: 411px; width: 126px; height: 132px; background: linear-gradient(170deg, #9cc4d8 0%, #6f8fb2 40%, #c98a5a 75%, #3f6c8a 100%); }
  .cover-rule-low { left: 126px; top: 411px; width: 6px; height: 132px; background: var(--orange); }
  .tagline { left: 134px; top: 411px; width: 250px; height: 24px; background: var(--blue); color: var(--white); font-size: 7.2px; font-weight: 300; line-height: 24px; padding-left: 8px; white-space: nowrap; }
  .brand { left: 158px; top: 452px; display: flex; align-items: center; gap: 9px; }
  .brand-dot { width: 50px; height: 50px; border-radius: 50%; background: var(--blue); flex: none; }
  .brand-name { font-family: var(--serif); font-weight: 600; font-size: 24px; line-height: 1; color: var(--orange); }
  .brand-sub { font-family: var(--serif); font-weight: 600; font-size: 11px; color: var(--blue); margin-top: 2px; }
  .cover-web { left: 290px; top: 519px; width: 94px; height: 16px; background: var(--orange); color: var(--white); font-size: 7.5px; font-weight: 300; line-height: 16px; padding-left: 10px; white-space: nowrap; }

  /* ---------- Story spread ---------- */
  .spread { left: 144px; top: 625px; width: 749px; height: 533px; }
  .photo-story { left: 0; top: 0; width: 488px; height: 533px; background: linear-gradient(100deg, #8fb9b8 0%, #3fb3b0 35%, #f0efe9 50%, #e8862b 70%, #d4662a 100%); }
  .story-head { left: 0; top: 0; width: 128px; height: 38px; background: var(--orange); color: var(--white); padding: 10px 0 0 16px; font-size: 20px; font-weight: 300; line-height: 1; white-space: nowrap; }
  .story-head small { font-size: 10px; }
  .story-panel { left: 0; top: 38px; width: 162px; height: 299px; background: rgba(255,255,255,.72); padding: 6px 8px 0 16px; }
  .body-copy { font-size: 8.4px; font-weight: 300; line-height: 12.3px; }
  .warranty-rule { left: 0; top: 338px; width: 320px; height: 6px; background: var(--orange); }
  .warranty-label { left: 0; top: 344px; width: 120px; height: 18px; background: var(--white); color: var(--blue); font-size: 10px; font-weight: 400; line-height: 18px; padding-left: 18px; white-space: nowrap; }
  .warranty-panel { left: 0; top: 362px; width: 162px; height: 171px; background: var(--blue); color: var(--white); padding: 8px 8px 0 16px; }
  .accent-blue { left: 181px; top: 0; width: 5px; height: 65px; background: var(--blue); }
  .accent-orange { left: 464px; top: 350px; width: 6px; height: 175px; background: var(--orange); }
  .story-base { left: 162px; top: 525px; width: 326px; height: 8px; background: var(--blue); }

  .catalog-side { left: 488px; top: 0; width: 261px; height: 533px; background: var(--white); }
  .side-rule { right: 0; top: 0; width: 7px; height: 305px; background: var(--orange); }
  .side-base { left: 0; bottom: 0; width: 261px; height: 8px; background: var(--blue); }
  .product { position: absolute; width: 100px; }
  .product-shot { width: 90px; height: 78px; border-radius: 4px; }
  .product-name { font-size: 5.4px; font-weight: 700; margin-top: 2px; }
  .product-desc { font-size: 5.2px; font-weight: 300; white-space: nowrap; }
  .shot-a { background: linear-gradient(160deg, #f4f4f4 40%, #3c5aa8 100%); }
  .shot-b { background: linear-gradient(160deg, #f2f2f2 40%, #2f4f9a 80%, #d6602c 100%); }
  .shot-c { background: linear-gradient(180deg, #f3f3f3 30%, #233e7e 100%); }
  .shot-d { background: linear-gradient(180deg, #efefef 30%, #222 70%, #444 100%); }
  .shot-e { background: linear-gradient(180deg, #f3f3f3 40%, #1f3a72 100%); }
  .shot-f { background: linear-gradient(150deg, #f2f2f2 40%, #c9303a 100%); }
</style>
</head>
<body>

<section class="page cover" aria-label="Front cover">
  <div class="abs photo-beach" role="img" aria-label="Lifestyle photo: mother and baby on a tropical beach with sailcloth bags"></div>
  <div class="abs photo-sail" role="img" aria-label="Photo: racing yacht under white sails on blue water"></div>
  <div class="abs cover-rule"></div>
  <div class="abs photo-tote" role="img" aria-label="Photo: white sailcloth tote with blue number six hanging on a yacht mast"></div>
  <div class="abs photo-flag" role="img" aria-label="Photo strip: waving American flag"></div>
  <div class="abs photo-family" role="img" aria-label="Lifestyle photo: mother holding baby beside a sailcloth tote at a marina"></div>
  <div class="abs cover-rule-low"></div>
  <p class="abs tagline">Travel Gear, Hand Bags and Decor Handcrafted in the USA with recycled yacht sails.</p>
  <div class="abs brand">
    <span class="brand-dot"></span>
    <div>
      <div class="brand-name">Morland Quist</div>
      <div class="brand-sub">Recycled Sailcloth Collection</div>
    </div>
  </div>
  <p class="abs cover-web">www.morlandquist.com</p>
</section>

<section class="page spread" aria-label="Company story spread">
  <div class="abs photo-story" role="img" aria-label="Lifestyle photo: smiling family with baby carrying a sailcloth messenger bag in front of a colourful beach hut"></div>
  <div class="abs accent-blue"></div>
  <h2 class="abs story-head">Morland's <small>Story</small></h2>
  <div class="abs story-panel">
    <p class="body-copy">Lorem ipsum dolor sit amet, consectetur adipisicing elit, sed do eiusmod tempor incididunt ut labore et dolore magna aliqua. Ut enim ad minim veniam, quis nostrud exercitation ullamco laboris nisi ut aliquip ex ea commodo consequat. Duis aute irure dolor in reprehenderit in voluptate velit esse cillum dolore eu fugiat nulla pariatur. Excepteur sint occaecat cupidatat non proident, sunt in culpa qui officia deserunt mollit anim id est laborum. Lorem ipsum dolor sit amet, consectetur adipisicing elit, sed do eiusmod tempor incididunt ut labore et dolore magna aliqua. Ut enim ad minim veniam, quis nostrud exercitation ullamco laboris nisi ut aliquip ex ea commodo consequat. Duis aute irure dolor in reprehenderit in voluptate velit esse cillum dolore eu fugiat nulla pariatur. Excepteur sint occaecat cupidatat non proident, sunt in culpa qui officia deserunt mollit anim id est laborum.</p>
  </div>
  <div class="abs warranty-rule"></div>
  <h3 class="abs warranty-label">Lifetime Warranty</h3>
  <div class="abs warranty-panel">
    <p class="body-copy">Lorem ipsum dolor sit amet, consectetur adipisicing elit, sed do eiusmod tempor incididunt ut labore et dolore magna aliqua. Ut enim ad minim veniam, quis nostrud exercitation ullamco laboris nisi ut aliquip ex ea commodo consequat. Duis aute irure dolor in reprehenderit in voluptate velit esse cillum dolore eu fugiat nulla pariatur. Excepteur sint occaecat cupidatat non proident, sunt in culpa qui officia deserunt mollit anim id est laborum.</p>
  </div>
  <div class="abs accent-orange"></div>
  <div class="abs story-base"></div>

  <div class="abs catalog-side">
    <div class="abs side-rule"></div>
    <div class="product" style="left:18px;top:28px"><div class="product-shot shot-a" role="img" aria-label="Product photo: sailcloth toiletry bag with blue number"></div><p class="product-name">PRODUCT NAME</p><p class="product-desc">Description to be place here</p></div>
    <div class="product" style="left:128px;top:20px"><div class="product-shot shot-b" role="img" aria-label="Product photo: sailcloth duffel with blue number and orange base"></div><p class="product-name">PRODUCT NAME</p><p class="product-desc">Description to be place here</p></div>
    <div class="product" style="left:18px;top:145px"><div class="product-shot shot-c" role="img" aria-label="Product photo: white tote with navy number"></div><p class="product-name">PRODUCT NAME</p><p class="product-desc">Description to be place here</p></div>
    <div class="product" style="left:128px;top:145px"><div class="product-shot shot-c" role="img" aria-label="Product photo: white tote with navy number"></div><p class="product-name">PRODUCT NAME</p><p class="product-desc">Description to be place here</p></div>
    <div class="product" style="left:18px;top:265px"><div class="product-shot shot-d" role="img" aria-label="Product photo: drawstring sea bag with black number"></div><p class="product-name">PRODUCT NAME</p><p class="product-desc">Description to be place here</p></div>
    <div class="product" style="left:128px;top:265px"><div class="product-shot shot-e" role="img" aria-label="Product photo: drawstring sea bag with navy number"></div><p class="product-name">PRODUCT NAME</p><p class="product-desc">Description to be place here</p></div>
    <div class="product" style="left:18px;top:410px"><div class="product-shot shot-f" role="img" aria-label="Product photo: sailcloth pillow with red numbers"></div><p class="product-name">PRODUCT NAME</p><p class="product-desc">Description to be place here</p></div>
    <div class="product" style="left:128px;top:410px"><div class="product-shot shot-a" role="img" aria-label="Product photo: sailcloth pillow with blue number"></div><p class="product-name">PRODUCT NAME</p><p class="product-desc">Description to be place here</p></div>
    <div class="abs side-base"></div>
  </div>
</section>

</body>
</html>
```